A online shop for solid wood need a Stationary design

A new online shop (in Austria and Germany) for solid wood and steel furniture (feldberg-formwerk) needs a Stationay design (letterhead, business card, envelope etc...). Dining tables, coffee tables, TV furniture and similar furniture will be sold. Everything will be custom made.

```html
<!DOCTYPE html>
<html lang="en">
<head>
<meta charset="utf-8">
<title>Feldberg Formwerk – Letterhead</title>
<link rel="stylesheet" href="https://fonts.googleapis.com/css2?family=Lato:wght@400;700&display=swap">
<style>
  :root {
    --backdrop: #e6e6e7;
    --paper-center: #ffffff;
    --paper-edge: #eeeef0;
    --brand-red: #e20a17;
    --ink: #3a3a3c;
    --band-black: #0c0c0c;
    --on-red: #ffffff;
    --signature-tone: #e4e4e7;
  }
  * { box-sizing: border-box; margin: 0; padding: 0; }
  html, body {
    width: 1154px;
    height: 1200px;
    overflow: hidden;
    background: var(--backdrop);
  }
  .letterhead {
    position: absolute;
    left: 181px;
    top: 40px;
    width: 791px;
    height: 1120px;
    background: radial-gradient(ellipse at 50% 35%, var(--paper-center) 0%, var(--paper-center) 30%, var(--paper-edge) 100%);
    box-shadow: 0 2px 8px rgba(0,0,0,0.18);
    overflow: hidden;
    font-family: "Lato", sans-serif;
    color: var(--ink);
  }
  .brand {
    position: absolute;
    left: 67px;
    top: 52px;
    display: flex;
    align-items: center;
    gap: 12px;
  }
  .brand-square {
    width: 30px;
    height: 30px;
    background: var(--brand-red);
  }
  .brand-name {
    font-family: "Lato", sans-serif;
    font-weight: 700;
    font-size: 28px;
    letter-spacing: 1px;
    color: var(--brand-red);
    text-transform: uppercase;
  }
  .letter-text {
    position: absolute;
    left: 67px;
    width: 670px;
    font-size: 15px;
    line-height: 18px;
  }
  .date { top: 246px; }
  .recipient { top: 283px; }
  .company { top: 337px; }
  .salutation {
    top: 412px;
    font-size: 19px;
    font-weight: 700;
  }
  .body-copy { top: 456px; }
  .body-copy p {
    text-align: justify;
    margin-bottom: 16px;
    line-height: 17px;
  }
  .closing { top: 766px; }
  .signature {
    position: absolute;
    left: 67px;
    top: 810px;
    width: 195px;
    height: 40px;
    background: linear-gradient(90deg, var(--signature-tone), rgba(228,228,231,0.3));
    border-radius: 4px;
  }
  .footer-wave {
    position: absolute;
    left: 0;
    bottom: 0;
    width: 791px;
    height: 200px;
  }
  .contact {
    position: absolute;
    left: 573px;
    top: 1003px;
    color: var(--on-red);
    font-size: 14px;
    line-height: 17px;
  }
  .contact-address { margin-bottom: 9px; }
  .contact-line {
    display: flex;
    align-items: center;
    gap: 10px;
    height: 17px;
  }
  .contact-line svg { width: 11px; height: 11px; }
</style>
</head>
<body>
  <main class="letterhead">
    <header class="brand">
      <span class="brand-square"></span>
      <span class="brand-name">Feldberg Formwerk</span>
    </header>

    <p class="letter-text date">Feb-03-2022</p>

    <p class="letter-text recipient">Mr, Paul Brenner<br>President</p>

    <p class="letter-text company">Harbor Lane Group<br>123 Street Name, Suite# 10<br>City, State, 120023</p>

    <h1 class="letter-text salutation">Dear Mr, Paul</h1>

    <section class="letter-text body-copy">
      <p>Lorem ipsum dolor sit amet, consectetur adipisicing elit, sed do eiusmod tempor incididunt ut labore et dolore magna aliqua. Ut enim ad minim veniam, quis nostrud exercitation ullamco laboris nisi ut aliquip ex ea commodo consequat. Duis aute irure dolor in reprehenderit in voluptate velit esse cillum dolore eu fugiat nulla pariatur.</p>
      <p>Lorem ipsum dolor sit amet, consectetur adipisicing elit, sed do eiusmod tempor incididunt ut labore et dolore magna aliqua. Ut enim ad minim veniam, quis nostrud exercitation ullamco laboris nisi ut aliquip ex ea commodo consequat. Duis aute irure dolor in reprehenderit in voluptate velit esse cillum dolore eu fugiat nulla pariatur.</p>
      <p>Lorem ipsum dolor sit amet, consectetur adipisicing elit, sed do eiusmod tempor incididunt ut labore et dolore magna aliqua. Ut enim ad minim veniam, quis nostrud exercitation ullamco laboris nisi ut aliquip ex ea commodo consequat.</p>
      <p>Excepteur sint occaecat cupidatat non proident, sunt in culpa qui officia deserunt mollit anim id est laborum. re et dolore magnam aliquam quaerat voluptatem.</p>
    </section>

    <p class="letter-text closing">Regards</p>

    <div class="signature" role="img" aria-label="Handwritten signature of Lukas Amsel"></div>

    <svg class="footer-wave" viewBox="0 1450 1247 315" preserveAspectRatio="none" aria-hidden="true">
      <path fill="var(--band-black)" d="M0,1640 C350,1600 700,1500 900,1480 C1050,1466 1180,1478 1247,1497 L1247,1522 C1170,1502 1050,1494 900,1506 C700,1525 350,1628 0,1658 Z"/>
      <path fill="var(--brand-red)" d="M0,1675 C350,1648 700,1548 950,1522 C1100,1508 1200,1522 1247,1538 L1247,1765 L0,1765 Z"/>
    </svg>

    <address class="contact" style="font-style: normal;">
      <div class="contact-address">418 Lindenweg,<br>Suite 12, Graz,<br>Steiermark 8010</div>
      <div class="contact-line">
        <svg viewBox="0 0 12 12" aria-hidden="true"><path fill="var(--on-red)" d="M2.4 0.8 L4.2 0.8 L5 3.4 L3.8 4.4 C4.4 5.8 5.6 7 7 7.6 L8 6.4 L10.8 7.2 L10.8 9.2 C10.8 10.2 10 11 9 10.9 C4.6 10.5 1.2 7.1 0.9 2.6 C0.8 1.6 1.5 0.8 2.4 0.8 Z"/></svg>
        <span>555-210-4873</span>
      </div>
      <div class="contact-line">
        <svg viewBox="0 0 12 12" aria-hidden="true"><rect x="3" y="0.8" width="6" height="3.2" fill="var(--on-red)"/><rect x="0.8" y="4.6" width="10.4" height="4.4" rx="1" fill="var(--on-red)"/><rect x="3" y="8" width="6" height="3.4" fill="var(--on-red)" stroke="var(--brand-red)" stroke-width="0.8"/></svg>
        <span>555-210-4890</span>
      </div>
    </address>
  </main>
</body>
</html>
```